Meadow Lantern Website

Here is the link for all the details, images and information you may need about our website:

https://www.filecrate.net/s/8pq42xk7m0zt3wd/OWEN%20HARGROVE.rar?dl=0

Here is a reference on our competitor: http://www.trekkora.com.au/ and we want as good as this one.

Number of Pages Required

1 page

```html
<!DOCTYPE html>
<html lang="en">
<head>
<meta charset="utf-8">
<title>Meadow Lantern</title>
<link href="https://fonts.googleapis.com/css2?family=Open+Sans:wght@400;600;700;800&display=swap" rel="stylesheet">
<style>
:root{
  --bg:#6e6254;
  --bg-dark:#5a4f43;
  --panel:#ffffff;
  --slider-bg:#eeeeee;
  --blue:#1a95d3;
  --blue-dark:#0f74b3;
  --red:#c9272d;
  --red-dark:#a81c22;
  --green:#1f9a45;
  --green-dark:#167a36;
  --orange:#e9a63a;
  --heading:#2a2a2a;
  --body:#6b6b6b;
  --foot-text:#f1ece4;
  --foot-bar:#4a4138;
}
*{margin:0;padding:0;box-sizing:border-box}
html,body{width:770px;height:1200px;overflow:hidden}
body{position:relative;font-family:"Open Sans",Arial,sans-serif;background:radial-gradient(ellipse at 50% 40%,#857767 0%,var(--bg) 55%,var(--bg-dark) 100%);color:var(--body)}
.abs{position:absolute}
.brand{left:0;width:770px;top:96px;text-align:center;font-weight:800;font-size:36px;color:#ffffff;letter-spacing:.5px}
.panel{left:64px;top:160px;width:643px;height:846px;background:var(--panel);border-radius:10px}
.tagline{left:70px;top:166px;width:632px;height:30px;border-radius:8px;background:linear-gradient(180deg,#36aee6,var(--blue-dark));color:#fff;font-size:12px;line-height:30px;text-align:center;letter-spacing:.2px}
.tagline b{font-weight:700}
.nav{left:70px;top:202px;width:632px;height:30px;border-radius:8px 8px 0 0;background:linear-gradient(180deg,#d8353a,var(--red-dark));display:flex;align-items:center;justify-content:center;gap:32px;list-style:none}
.nav li{color:#fff;font-size:8px;font-weight:700;letter-spacing:.2px}
.slider{left:70px;top:232px;width:632px;height:224px;background:var(--slider-bg);border-radius:0 0 8px 8px}
.slide{top:240px;width:200px;height:208px;border-radius:6px;overflow:hidden}
.slide .photo{position:absolute;inset:0}
.slide .cap{position:absolute;left:0;right:0;bottom:0;height:46px;background:rgba(15,15,15,.88);padding:11px 12px 0}
.cap h3{color:#fff;font-size:9px;font-weight:700;letter-spacing:.1px}
.cap p{color:#e6e6e6;font-size:7px;margin-top:6px;display:flex;align-items:center;gap:4px}
.dot{width:7px;height:7px;border-radius:50%;background:#f08a1c;display:inline-block}
.arrow{top:335px;width:16px;height:16px;background:var(--red);display:flex;align-items:center;justify-content:center}
h2.sec{position:absolute;font-size:11.5px;font-weight:700;color:var(--heading);letter-spacing:.2px}
.txt{position:absolute;font-size:7.2px;line-height:14.4px;color:var(--body)}
.video{left:78px;top:502px;width:176px;height:124px;background:linear-gradient(180deg,#6aa6d8 0%,#9cc6e6 30%,#2f8ab0 48%,#3d7a3a 75%,#2b5a2a 100%)}
.player{left:78px;top:614px;width:176px;height:12px;background:#f2f2f2;border:1px solid #ccc}
.label{position:absolute;font-size:7px;font-weight:700;color:#444}
.input{position:absolute;left:78px;width:176px;height:21px;border:1px solid #d4d4d4;border-radius:2px;font-size:7px;color:#777;padding:6px 8px;background:#fff}
.input svg{position:absolute;right:6px;top:4px}
.btn{position:absolute;height:20px;background:linear-gradient(180deg,#26a94e,var(--green-dark));color:#fff;font-size:7px;font-weight:700;display:flex;align-items:center;justify-content:center;border-radius:2px}
.tile{position:absolute;width:130px;height:85px;border-radius:5px;overflow:hidden}
.tile .photo{position:absolute;left:0;right:0;top:0;height:63px}
.tile .bar{position:absolute;left:0;right:0;bottom:0;height:22px;background:var(--orange);color:#fff;font-size:7.5px;padding:6px 12px 0}
.thumb{position:absolute;top:819px;width:130px;height:72px}
.footer h4{position:absolute;top:1035px;font-size:9.5px;font-weight:700;color:#fff}
.flinks{position:absolute;top:1052px;list-style:none;font-size:7px;line-height:14.4px;color:var(--foot-text)}
.social{position:absolute;top:1073px;width:19px;height:19px;border-radius:50%;background:#fff}
.card{position:absolute;top:1109px;height:14px;background:#fff;border:1px solid #ddd}
.copy{left:0;top:1172px;width:770px;height:28px;background:var(--foot-bar);color:#e8e1d6;font-size:7px;text-align:center;line-height:28px}
</style>
</head>
<body>
<div class="abs brand">Meadow Lantern</div>

<div class="abs panel"></div>
<div class="abs tagline"><b>EXPERIENCE CAIRNS AT ITS BEST</b> AND A TASTE OF TRUE AUTHENTIC ABORIGINAL CULTURE!</div>
<ul class="abs nav">
  <li>HOME</li><li>BOOK ONLINE</li><li>ACCOMMODATION</li><li>EXTRA TOURS</li><li>ENQUERY BOOKING</li><li>TESTIMONIALS</li><li>CONTACT</li>
</ul>
<div class="abs slider"></div>

<div class="abs slide" style="left:78px">
  <div class="photo" role="img" aria-label="Photo of visitors at a giant crocodile sculpture" style="background:linear-gradient(160deg,#8ea0a8,#9a8f7e 50%,#5f6a55)"></div>
  <div class="cap"><h3>ONE BEING THE CROCODILE</h3><p>View the Details <span class="dot"></span></p></div>
</div>
<div class="abs slide" style="left:286px">
  <div class="photo" role="img" aria-label="Photo of a man on rocks beside a waterfall" style="background:linear-gradient(170deg,#3a3a30,#6e6a5c 45%,#c9ccc6 70%,#4c4a40)"></div>
  <div class="cap"><h3>WATERFALL</h3><p>View the Details <span class="dot"></span></p></div>
</div>
<div class="abs slide" style="left:494px">
  <div class="photo" role="img" aria-label="Photo of an Aboriginal man playing the didgeridoo by a fire at night" style="background:linear-gradient(180deg,#0e0c0a,#2a1a10 50%,#b5561a 80%,#e07d2a)"></div>
  <div class="cap"><h3>THE ABORIGINAL PLAYING THE DIDGJI</h3><p>View the Details <span class="dot"></span></p></div>
</div>
<div class="abs arrow" style="left:80px"><svg width="6" height="9" viewBox="0 0 6 9"><path d="M5 1 1 4.5 5 8" fill="none" stroke="#fff" stroke-width="1.3"/></svg></div>
<div class="abs arrow" style="left:677px"><svg width="6" height="9" viewBox="0 0 6 9"><path d="M1 1 5 4.5 1 8" fill="none" stroke="#fff" stroke-width="1.3"/></svg></div>

<h2 class="sec" style="left:78px;top:476px">OUR VIDEOS</h2>
<div class="abs video" role="img" aria-label="Video still of a tropical beach and coastline"></div>
<svg class="abs" style="left:153px;top:543px" width="26" height="26" viewBox="0 0 26 26"><rect width="26" height="26" rx="2" fill="#1f3d5c" opacity=".85"/><path d="M9 7 19 13 9 19Z" fill="#4aa0d8"/></svg>
<div class="abs player">
  <svg width="176" height="10" viewBox="0 0 176 10"><path d="M4 2 8 5 4 8Z" fill="#222"/><text x="18" y="7.5" font-size="5.5" font-family="Open Sans,sans-serif" fill="#333">00:00</text><rect x="38" y="4" width="100" height="2" fill="#999"/><text x="142" y="7.5" font-size="5.5" font-family="Open Sans,sans-serif" fill="#333">00:00</text><path d="M160 3 163 5 160 7Z" fill="#444"/><rect x="168" y="3" width="4" height="4" fill="none" stroke="#444" stroke-width=".8"/></svg>
</div>

<h2 class="sec" style="left:78px;top:643px">BOOK ONLINE</h2>
<p class="txt" style="left:78px;top:665px;width:180px">Lorem Ipsum is simply dummy text of the printing and typesetting industry.</p>
<span class="label" style="left:82px;top:703px">FROM</span>
<div class="input" style="top:718px">dd - mmm - yyyy<svg width="12" height="12" viewBox="0 0 12 12"><rect x="1" y="2" width="10" height="9" fill="none" stroke="#bbb"/><path d="M1 5h10M4 1v2M8 1v2" stroke="#bbb"/></svg></div>
<span class="label" style="left:82px;top:749px">TO</span>
<div class="input" style="top:763px">dd - mmm - yyyy<svg width="12" height="12" viewBox="0 0 12 12"><rect x="1" y="2" width="10" height="9" fill="none" stroke="#bbb"/><path d="M1 5h10M4 1v2M8 1v2" stroke="#bbb"/></svg></div>
<div class="btn" style="left:78px;top:796px;width:87px">BOOK NOW</div>

<h2 class="sec" style="left:78px;top:843px">ABOUT MEADOW LANTERN</h2>
<p class="txt" style="left:78px;top:865px;width:180px">Lorem Ipsum is simply dummy text of the printing and typesetting industry. Lorem Ipsum has been the industry's standard dummy text.</p>
<p class="txt" style="left:78px;top:922px;width:180px">Took a galley of type and scrambled it to make a type specimen book....</p>
<div class="btn" style="left:78px;top:966px;width:66px">READ MORE</div>

<h2 class="sec" style="left:278px;top:476px">WHY WE ARE THE BEST?</h2>
<p class="txt" style="left:278px;top:497px;width:420px">Lorem Ipsum is simply dummy text of the printing and typesetting industry. Lorem Ipsum has been the industry's standard dummy text ever since the 1500s, when an unknown printer took a galley of type and scrambled it to make a type specimen book. It has survived not only five centuries, but also the leap into electronic typesetting, remaining essentially unchanged. It was popularised in the 1960s with the release of Lettrafine sheets containing Lorem Ipsum passages, and more recently with desktop publishing software like Pagecraft Studio including versions of Lorem Ipsum.</p>

<div class="tile" style="left:278px;top:591px"><div class="photo" role="img" aria-label="Photo of a man on a rock in the rainforest" style="background:linear-gradient(180deg,#3f6a32,#7e8f6a 60%,#6e6e66)"></div><div class="bar">EXPERIENCE</div></div>
<div class="tile" style="left:420px;top:591px"><div class="photo" role="img" aria-label="Photo of a green hillside and calm water" style="background:linear-gradient(180deg,#d8dcd6,#5e7f45 45%,#8aa884 75%,#b0c4bc)"></div><div class="bar">SIGHT- SEEING</div></div>
<div class="tile" style="left:565px;top:591px"><div class="photo" role="img" aria-label="Photo of kangaroos on a grassy field" style="background:linear-gradient(180deg,#4f7238,#8ea65a 50%,#7a8d4a)"></div><div class="bar">PARTICIPATE</div></div>
<div class="tile" style="left:278px;top:692px"><div class="photo" role="img" aria-label="Photo of two travellers in the forest" style="background:linear-gradient(180deg,#3d5c30,#8a8a78 55%,#5a6a52)"></div><div class="bar">TWO SPECTACULAR</div></div>
<div class="tile" style="left:420px;top:692px"><div class="photo" role="img" aria-label="Photo of a group at river boulders" style="background:linear-gradient(180deg,#2c3a24,#6a6658 50%,#a8a89e)"></div><div class="bar">FISHING GROUP</div></div>
<div class="tile" style="left:565px;top:692px"><div class="photo" role="img" aria-label="Photo of people swimming in a forest stream" style="background:linear-gradient(180deg,#4a6a3a,#9aa88a 50%,#b09070 75%,#7a8a6a)"></div><div class="bar">SWIM</div></div>

<h2 class="sec" style="left:278px;top:797px;font-size:10px">ACTIVITIES</h2>
<h2 class="sec" style="left:422px;top:797px;font-size:10px">ACCOMADATION</h2>
<h2 class="sec" style="left:566px;top:797px;font-size:10px">PACKAGES</h2>
<div class="thumb" role="img" aria-label="Photo of a warmly lit lodge interior" style="left:278px;background:linear-gradient(160deg,#2a120a,#7a3a1a 45%,#c9863a 70%,#3a1a0e)"></div>
<div class="thumb" role="img" aria-label="Photo of guests around an evening campfire" style="left:422px;background:linear-gradient(180deg,#140c08,#3a2014 50%,#c8702a 80%,#f0b050)"></div>
<div class="thumb" role="img" aria-label="Photo of a giant crocodile sculpture tour stop" style="left:565px;background:linear-gradient(160deg,#a8b8c0,#9a958a 50%,#6a7558)"></div>
<p class="txt" style="left:278px;top:897px;width:132px">Lorem Ipsum is simply dummy text of the printing and typesetting industry. Lorem Ipsum has been the industry's standard dummy...</p>
<p class="txt" style="left:422px;top:897px;width:132px">Lorem Ipsum is simply dummy text of the printing and typesetting industry. Lorem Ipsum has been the industry's standard dummy...</p>
<p class="txt" style="left:565px;top:897px;width:132px">Lorem Ipsum is simply dummy text of the printing and typesetting industry. Lorem Ipsum has been the industry's standard dummy...</p>
<div class="btn" style="left:278px;top:966px;width:65px">READ MORE</div>
<div class="btn" style="left:422px;top:966px;width:65px">READ MORE</div>
<div class="btn" style="left:565px;top:966px;width:65px">READ MORE</div>

<footer class="footer">
  <h4 style="left:79px">WELCOME</h4>
  <ul class="flinks" style="left:79px"><li>Home</li><li>Book online</li><li>Accommodation</li><li>Extra Tours</li><li>Enquery Booking</li><li>Testimonials</li><li>Contact</li></ul>
  <h4 style="left:222px">INFORMATION</h4>
  <ul class="flinks" style="left:222px"><li>Terms &amp; Condition</li><li>Privacy policy</li><li>Disclaimer</li><li>Sitemap</li></ul>
  <h4 style="left:366px">CONTACT INFO</h4>
  <ul class="flinks" style="left:366px"><li>120 Street name, City name,</li><li>Country name - 3236523.</li></ul>
  <svg class="abs" style="left:367px;top:1088px" width="8" height="8" viewBox="0 0 8 8"><path d="M1.5 .5 3 2.3 2.2 3.3C2.8 4.6 3.6 5.3 4.8 5.9L5.7 5 7.5 6.5 6.6 7.5C3.5 7.2.8 4.6.5 1.4Z" fill="#fff"/></svg>
  <span class="abs" style="left:381px;top:1086px;font-size:7px;color:var(--foot-text)">0412 555 018</span>
  <svg class="abs" style="left:367px;top:1105px" width="9" height="7" viewBox="0 0 9 7"><rect width="9" height="7" fill="#fff"/><path d="M0 0 4.5 4 9 0" fill="none" stroke="#6e6254" stroke-width=".8"/></svg>
  <span class="abs" style="left:381px;top:1103px;font-size:7px;color:var(--foot-text)">info@meadowlantern.com.au</span>
  <h4 style="left:542px">FOLLOW US</h4>
  <ul class="flinks" style="left:542px"><li>Connect with our social network</li></ul>
  <div class="social" style="left:543px"></div><div class="social" style="left:566px"></div><div class="social" style="left:590px"></div><div class="social" style="left:613px"></div><div class="social" style="left:636px"></div>
  <div class="card" style="left:545px;width:34px"></div><div class="card" style="left:583px;width:26px"></div><div class="card" style="left:613px;width:22px"></div><div class="card" style="left:641px;width:23px"></div>
</footer>
<div class="abs copy">© Copyright 2015. Meadow Lantern. All rights reserved.</div>
</body>
</html>
```